MOLT - Monitoring Natural Hazards from Space Web Application

KORVEN Sarl is a Luxembourg based Space-Startup that works in the field of Earth Observation. KORVEN is a platform able to extract value-added information from satellite data and is specialized in mapping Natural Disaster (floods, fires etc).

We are now developing a new vertical tool, called MOLT, dedicated to the monitoring of natural hazards in Humanitarian Camps around the world.

The goal of MOLT is to hide to the users' all the complexity of the Satellite Image processing and just provide them the results.

This project require to Design 4 pages of MOLT:
• Public Home Page (Code - V01)
• Dashboard (private Home Page) (Code - V03)
• Monitor (web GIS) (Code - V14)
• Registration Page (Code - V04)

We would like to provide the required time to make a good job.

Target Market(s)

Humanitarian Agencies, Goverments

Coding

Coded - Design and coding required

Number of Pages Required

4 page

Font styles to use
Other font styles liked:
• see the manual attached

Requirements
Must have
• 4 pages. One Home, one form, one dashboard and one web map.
Nice to have
• Please read the attachment with all the detailed instructions

```html
<!DOCTYPE html>
<html lang="en">
<head>
<meta charset="utf-8">
<title>MOLT – Web Application Pages</title>
<link href="https://fonts.googleapis.com/css2?family=Poppins:wght@400;500;600;700&family=Figtree:ital,wght@0,400;0,500;0,600;0,700;1,400&family=Space+Mono&family=Archivo:wght@400;900&display=swap" rel="stylesheet">
<style>
:root{
  --canvas:#dfe3ea;
  --panel:#f1f2f4;
  --white:#ffffff;
  --yellow:#f0b92e;
  --teal:#264a5a;
  --teal-dark:#1d3c49;
  --ink:#1f3440;
  --text:#4b5a63;
  --muted:#8b969c;
  --line:#d9dde1;
  --footer:#0f1f26;
  --footer-bar:#13272f;
  --sea:#6fb2c6;
  --sea-light:#8cc0cf;
  --land:#b9cbb4;
}
*{box-sizing:border-box;margin:0;padding:0}
html,body{width:938px;height:1200px;overflow:hidden}
body{background:var(--canvas);font-family:"Figtree",sans-serif;color:var(--ink);position:relative}
.abs{position:absolute}
.page-title{position:absolute;font-family:"Poppins",sans-serif;font-weight:600;font-size:13px;color:var(--teal);transform:translateX(-50%);white-space:nowrap}
.page-title span{color:var(--yellow)}

/* brand */
.brand{position:absolute;display:flex;align-items:center;gap:5px;font-family:"Poppins",sans-serif;font-weight:500;color:var(--teal);letter-spacing:1.5px}
.brand-dot{border-radius:50%;border:1.5px solid var(--yellow);background:var(--white)}

/* ================= HOME ================= */
.home{left:46px;top:37px;width:411px;height:1114px;background:var(--white);overflow:hidden}
.hero{position:absolute;left:0;top:0;width:411px;height:225px;background:radial-gradient(ellipse 120% 55% at 50% 110%,#3b86b8 0%,#1b4468 28%,#0c1d33 50%,#06101c 75%)}
.navbar{position:absolute;left:29px;top:15px;width:352px;height:23px;background:var(--white);display:flex;align-items:center}
.nav-links{position:absolute;left:167px;top:0;height:23px;display:flex;align-items:center;gap:11px;font-size:5.6px;color:var(--ink)}
.btn{display:flex;align-items:center;justify-content:center;font-size:5.6px;font-weight:500}
.btn-yellow{background:var(--yellow);color:var(--ink)}
.btn-teal{background:var(--teal);color:var(--white)}
.hero-kicker{position:absolute;left:0;width:411px;top:51px;text-align:center;font-family:"Space Mono",monospace;font-size:8px;color:var(--yellow)}
.hero-title{position:absolute;left:0;width:411px;top:63px;text-align:center;font-family:"Poppins",sans-serif;font-weight:600;font-size:19.5px;line-height:25px;color:var(--white)}
.hero-cta{position:absolute;left:177px;top:121px;width:57px;height:14px}
.dots{position:absolute;display:flex;gap:3px;align-items:center}
.dots i{display:block;width:2px;height:2px;border-radius:50%;background:var(--white)}
.dots i.on{width:16px;height:1.5px;border-radius:1px;background:var(--yellow)}

.trust{position:absolute;left:0;top:225px;width:411px;height:89px;background:var(--white)}
.trust h3{position:absolute;top:20px;width:100%;text-align:center;font-size:6.6px;font-weight:600;color:var(--ink)}
.partner{position:absolute;top:40px;width:32px;height:30px}

.tool{position:absolute;left:0;top:314px;width:411px;height:225px;background:#eef0f3}
.eyebrow{font-family:"Space Mono",monospace;font-size:4.6px;color:var(--ink);letter-spacing:.3px}
.section-heading{font-family:"Poppins",sans-serif;font-weight:600;font-size:14.5px;color:var(--yellow)}
.tool .eyebrow{position:absolute;left:29px;top:40px}
.tool .section-heading{position:absolute;left:29px;top:48px}
.tool-copy{position:absolute;left:29px;top:71px;width:174px;font-size:5.4px;line-height:8px;color:var(--text)}
.feature{position:absolute;left:29px;width:180px;height:30px}
.feature-icon{position:absolute;left:0;top:0;width:28px;height:28px;border-radius:50%;border:1px solid var(--yellow);background:var(--white)}
.feature h4{position:absolute;left:37px;top:1px;font-size:6.4px;font-weight:500;color:var(--ink)}
.feature p{position:absolute;left:37px;top:11px;width:140px;font-size:5.3px;line-height:8px;color:var(--text)}
.emblem{position:absolute;left:224px;top:39px;width:157px;height:157px;border-radius:50%;background:var(--teal);display:flex;align-items:center;justify-content:center;font-family:"Poppins",sans-serif;font-weight:600;font-size:30px;letter-spacing:4px;color:var(--yellow)}

.pricing{position:absolute;left:0;top:539px;width:411px;height:226px;background:var(--white)}
.pricing .eyebrow,.stories .eyebrow{position:absolute;width:100%;text-align:center}
.pricing .eyebrow{top:16px}
.pricing .section-heading,.stories .section-heading{position:absolute;width:100%;text-align:center}
.pricing .section-heading{top:22px}
.plan{position:absolute;top:54px;width:107px;height:146px;background:var(--white);box-shadow:0 1px 5px rgba(20,40,50,.12)}
.plan.featured{top:48px;height:159px;background:var(--teal)}
.plan-name{position:absolute;left:12px;top:14px;font-family:"Poppins",sans-serif;font-weight:600;font-size:7px;color:var(--ink)}
.plan-sub{position:absolute;left:12px;top:23px;font-size:5px;color:var(--muted)}
.plan-price{position:absolute;right:-6px;top:16px;height:11px;padding:0 5px;background:var(--yellow);color:var(--white);font-size:5.4px;font-weight:600;display:flex;align-items:center}
.plan-rule{position:absolute;left:12px;right:6px;top:38px;height:1px;background:var(--line)}
.plan-list{position:absolute;left:9px;top:47px;list-style:none}
.plan-list li{display:flex;align-items:center;gap:5px;height:14px;font-size:5.4px;color:var(--text)}
.tick{width:5px;height:5px;background:var(--teal);border-radius:.6px;position:relative;flex:none}
.tick::after{content:"";position:absolute;left:1.6px;top:.7px;width:1.2px;height:2.3px;border:solid var(--white);border-width:0 .7px .7px 0;transform:rotate(45deg)}
.plan.featured .plan-name{color:var(--white)}
.plan.featured .plan-sub{color:#d9e2e6}
.plan.featured .plan-rule{background:#3e6272}
.plan.featured .plan-list li{color:var(--white)}
.plan.featured .tick{background:var(--yellow)}
.plan.featured .plan-price{right:-10px}
.plan-btn{position:absolute;left:9px;width:90px;height:15px;top:120px}
.plan.featured .plan-btn{top:126px}

.stories{position:absolute;left:0;top:765px;width:411px;height:202px;background:#eef0f3}
.stories .eyebrow{top:22px}
.stories .section-heading{top:28px}
.story{position:absolute;top:61px;width:113px;height:93px;background:var(--white)}
.quote-mark{position:absolute;left:10px;top:6px;font-family:"Poppins",sans-serif;font-size:20px;line-height:20px;color:var(--teal)}
.story p{position:absolute;left:10px;top:26px;width:96px;font-size:5.4px;line-height:8.2px;font-style:italic;color:var(--text)}
.stars{position:absolute;left:10px;top:61px;font-size:5.5px;letter-spacing:.5px;color:var(--yellow)}
.avatar{position:absolute;left:10px;top:74px;width:15px;height:15px;border-radius:50%;background:linear-gradient(135deg,#c9ced3,#6f7b84)}
.story-name{position:absolute;left:29px;top:75px;font-size:5.6px;font-weight:600;color:var(--ink)}
.story-role{position:absolute;left:29px;top:82px;font-size:4.4px;color:var(--muted)}

.site-footer{position:absolute;left:0;top:967px;width:411px;height:148px;background:var(--footer)}
.foot-col{position:absolute;top:24px}
.foot-col h5{font-size:5.6px;font-weight:600;color:var(--yellow);margin-bottom:9px}
.foot-col ul{list-style:none}
.foot-col li{font-size:5px;color:#d2dade;height:11.8px}
.foot-contact li{display:flex;gap:6px;align-items:flex-start;line-height:9.5px;height:auto;margin-bottom:2px}
.foot-contact svg{flex:none;margin-top:2px}
.foot-text{width:82px;font-size:5px;line-height:8.6px;color:#d2dade}
.social{display:flex;gap:7px}
.social i{display:block;width:7px;height:7px;border-radius:50%;background:#dfe6ea}
.foot-bar{position:absolute;left:29px;top:110px;width:352px;height:26px;background:var(--footer-bar)}
.foot-bar .copy{position:absolute;left:0;width:100%;top:0;line-height:26px;text-align:center;font-size:4.6px;color:#cdd6da}
.foot-bar .copy b,.small-copy b{font-weight:400;color:var(--yellow)}
.foot-bar .stamp{position:absolute;right:8px;top:0;line-height:26px;font-size:4.4px;color:#5c7d8a}

/* ================= APP PANELS ================= */
.app-panel{position:absolute;left:482px;width:410px;background:var(--panel)}
.app-bar{position:absolute;left:29px;top:15px;width:352px;height:22px;background:var(--white)}
.app-tools{position:absolute;right:5px;top:4px;height:14px;display:flex;align-items:center;gap:5px}
.lang{font-size:5.8px;color:var(--ink);margin:0 5px 0 2px}
.icon-btn{width:14px;height:14px;border:1px solid var(--teal);background:var(--white);display:flex;align-items:center;justify-content:center}
.icon-btn.fill{background:var(--yellow);border-color:var(--yellow)}
.logout{height:14px;padding:0 7px;gap:3px}
.small-copy{position:absolute;left:0;width:100%;text-align:center;font-size:4.4px;color:var(--ink)}

.side-card{position:absolute;left:29px;width:84px;background:var(--white)}
.side-head{height:14px;background:var(--teal);color:var(--white);font-size:5px;font-weight:600;padding-left:5px;display:flex;align-items:center}
.stat{display:flex;align-items:center;gap:6px;padding:5px 5px}
.stat-num{font-family:"Poppins",sans-serif;font-weight:500;font-size:8px;color:var(--yellow);line-height:9px}
.stat-label{font-size:4.2px;color:var(--ink)}
.row-item{display:flex;align-items:center;gap:5px;margin:0 5px;height:21px;border-bottom:1px solid var(--line)}
.row-item:last-child{border-bottom:0}
.row-icon{width:14px;height:14px;border-radius:50%;border:1px solid #9aa5ab;flex:none;display:flex;align-items:center;justify-content:center}
.row-text{font-size:5px;line-height:6px;color:var(--ink)}
.row-text small{display:block;font-size:3.4px;color:var(--muted);line-height:5px}
.map{position:absolute;left:122px;top:51px;width:259px;height:189px;background:linear-gradient(100deg,var(--sea) 0%,var(--sea-light) 45%,var(--land) 100%)}
.map-ctrls{position:absolute;right:4px;top:10px;display:flex;flex-direction:column;gap:3px}
.map-ctrls i,.zoom{display:block;width:12px;height:12px;background:var(--white);border-radius:1.5px}
.zoom{position:absolute;right:4px;bottom:4px;height:22px;font-size:7px;line-height:10px;text-align:center;color:var(--ink)}

.reg-card{position:absolute;left:29px;top:46px;width:352px;height:239px;background:var(--white)}
.reg-card h2{position:absolute;left:11px;top:4px;font-family:"Poppins",sans-serif;font-weight:600;font-size:11px;color:var(--ink)}
.field label{position:absolute;font-size:5px;font-weight:500;color:var(--ink);white-space:nowrap}
.field label span{font-weight:400}
.field .input{position:absolute;height:15px;background:#f3f4f5;border:1px solid #d3d7da;font-size:4.4px;color:#5a666d;padding-left:5px;display:flex;align-items:center}
.check{position:absolute;left:11px;display:flex;align-items:center;gap:5px;font-size:5px;color:var(--ink)}
.check i{display:block;width:5px;height:5px;border:1px solid #b9bfc3}
.reg-btn{position:absolute;left:296px;top:215px;width:45px;height:15px}

.layer-list{position:absolute;left:29px;top:51px;width:84px;height:72px;background:var(--white)}
.layer-list ul{list-style:none;padding:0 5px}
.layer-list li{height:13px;border-bottom:1px solid var(--line);font-size:4.8px;display:flex;align-items:center;justify-content:space-between;color:var(--ink)}
.layer-list li:last-child{border-bottom:0}
.map-toolbar{position:absolute;left:85px;top:8px;width:90px;height:14px;background:var(--teal);border-radius:2px;display:flex;align-items:center;justify-content:space-around}
.map-toolbar i{display:block;width:5px;height:5px;background:var(--yellow);border-radius:1px}

.thanks{position:absolute;left:482px;width:410px;text-align:center}
.thanks-top{top:1022px;font-family:"Archivo",sans-serif;font-weight:400;font-size:18px;color:var(--ink);letter-spacing:.5px}
.thanks-big{top:1042px;font-family:"Archivo",sans-serif;font-weight:900;font-size:49px;color:var(--yellow);letter-spacing:.5px}
</style>
</head>
<body>

<div class="page-title" style="left:251px;top:11px">Home <span>Page</span></div>
<div class="page-title" style="left:687px;top:11px">Dashboard</div>
<div class="page-title" style="left:687px;top:318px">Registration Page</div>
<div class="page-title" style="left:687px;top:668px">Registration Page</div>

<!-- ============ HOME PAGE ============ -->
<main class="abs home">
  <section class="hero" role="img" aria-label="Night view of Earth from orbit with city lights and a glowing horizon">
    <nav class="navbar">
      <div class="brand" style="left:5px;top:3px;font-size:12px"><i class="brand-dot" style="width:17px;height:17px"></i>MOLT</div>
      <div class="nav-links"><span>Home</span><span>Features</span><span>Pricing</span></div>
      <div class="btn btn-yellow abs" style="left:255px;top:3px;width:45px;height:16px">Register</div>
      <div class="btn btn-teal abs" style="left:305px;top:3px;width:43px;height:16px">Login</div>
    </nav>
    <p class="hero-kicker">Dedicated to the monitoring of natural</p>
    <h1 class="hero-title">Hazards In Humanitarian<br>Camps Around The World</h1>
    <div class="btn btn-yellow hero-cta">Discover More</div>
    <div class="dots" style="left:192px;top:208px"><i class="on"></i><i></i><i></i></div>
  </section>

  <section class="trust">
    <h3>They Trust in Us</h3>
    <svg class="partner" style="left:30px" viewBox="0 0 32 30"><rect x="4" y="4" width="24" height="20" fill="#c9ced2"/></svg>
    <svg class="partner" style="left:96px" viewBox="0 0 32 30"><circle cx="16" cy="14" r="11" fill="#c9ced2"/></svg>
    <svg class="partner" style="left:159px" viewBox="0 0 32 30"><rect x="5" y="3" width="22" height="22" fill="#c9ced2"/></svg>
    <svg class="partner" style="left:221px" viewBox="0 0 32 30"><circle cx="16" cy="14" r="11" fill="#c9ced2"/></svg>
    <svg class="partner" style="left:288px" viewBox="0 0 32 30"><rect x="3" y="5" width="26" height="18" fill="#c9ced2"/></svg>
    <svg class="partner" style="left:352px" viewBox="0 0 32 30"><circle cx="16" cy="14" r="11" fill="#c9ced2"/></svg>
  </section>

  <section class="tool">
    <p class="eyebrow">TOOL DESCRIPTION</p>
    <h2 class="section-heading">Description Of The Tool</h2>
    <p class="tool-copy">Lorem ipsum dolor sit amet, constetur adipiscing elit, sed do eiusmod tempor incididunt ut labore et dolore mliqua. Quis ipsum suspendisse ultrices gravida. Risus commodo viverra maecenas accumsan lacus vel facilisis.</p>
    <div class="feature" style="top:112px">
      <div class="feature-icon"></div>
      <h4>Praesent ut viverra</h4>
      <p>Vestibulum ac tristique risus. Integer quis mauris magna. Proin risus leo, aliquam vel dignissim in</p>
    </div>
    <div class="feature" style="top:153px">
      <div class="feature-icon"></div>
      <h4>Donec purus enim</h4>
      <p>Vestibulum ac tristique risus. Integer quis mauris magna. Proin risus leo, aliquam vel dignissim in</p>
    </div>
    <div class="emblem">MOLT</div>
  </section>

  <section class="pricing">
    <p class="eyebrow">PRICING</p>
    <h2 class="section-heading">Pricing List</h2>

    <article class="plan" style="left:29px">
      <h3 class="plan-name">BASIC</h3><p class="plan-sub">Lorem ipsum dolor</p>
      <span class="plan-price">$38.99</span><div class="plan-rule"></div>
      <ul class="plan-list">
        <li><i class="tick"></i>Aliquam semper quam at nisi</li>
        <li><i class="tick"></i>Sollicitudin vel tincidunt mauris</li>
        <li><i class="tick"></i>Vivamus vehicula pretium lacus</li>
        <li><i class="tick"></i>Proin risus leo, aliquam vel</li>
        <li><i class="tick"></i>Mauris scelerisquerhoncus</li>
      </ul>
      <div class="btn btn-yellow plan-btn">Select Now</div>
    </article>

    <article class="plan featured" style="left:149px">
      <h3 class="plan-name" style="top:20px">PREMIUM</h3><p class="plan-sub" style="top:29px">Lorem ipsum dolor</p>
      <span class="plan-price" style="top:22px">$158.99</span><div class="plan-rule" style="top:44px"></div>
      <ul class="plan-list" style="top:53px">
        <li><i class="tick"></i>Aliquam semper quam at nisi</li>
        <li><i class="tick"></i>Sollicitudin vel tincidunt mauris</li>
        <li><i class="tick"></i>Vivamus vehicula pretium lacus</li>
        <li><i class="tick"></i>Proin risus leo, aliquam vel</li>
        <li><i class="tick"></i>Mauris scelerisquerhoncus</li>
      </ul>
      <div class="btn btn-yellow plan-btn">Select Now</div>
    </article>

    <article class="plan" style="left:269px">
      <h3 class="plan-name">STANDARD</h3><p class="plan-sub">Lorem ipsum dolor</p>
      <span class="plan-price">$288.99</span><div class="plan-rule"></div>
      <ul class="plan-list">
        <li><i class="tick"></i>Aliquam semper quam at nisi</li>
        <li><i class="tick"></i>Sollicitudin vel tincidunt mauris</li>
        <li><i class="tick"></i>Vivamus vehicula pretium lacus</li>
        <li><i class="tick"></i>Proin risus leo, aliquam vel</li>
        <li><i class="tick"></i>Mauris scelerisquerhoncus</li>
      </ul>
      <div class="btn btn-yellow plan-btn">Select Now</div>
    </article>
  </section>

  <section class="stories">
    <p class="eyebrow">TESTIMONIALS</p>
    <h2 class="section-heading">Our Success Story</h2>
    <article class="story" style="left:29px">
      <span class="quote-mark">“</span>
      <p>Nunc volutpat fringilla ipsum, a cursus ligula ultrices sed. Aenean in erat ante. Maecenas tincidunt mauris ac massa viverra.</p>
      <span class="stars">★★★★★</span>
      <i class="avatar" role="img" aria-label="Customer portrait"></i>
      <span class="story-name">Dana Holt</span><span class="story-role">Customer</span>
    </article>
    <article class="story" style="left:149px">
      <span class="quote-mark">“</span>
      <p>Nunc volutpat fringilla ipsum, a cursus ligula ultrices sed. Aenean in erat ante. Maecenas tincidunt mauris ac massa viverra.</p>
      <span class="stars">★★★★★</span>
      <i class="avatar" role="img" aria-label="Customer portrait"></i>
      <span class="story-name">Dana Holt</span><span class="story-role">Customer</span>
    </article>
    <article class="story" style="left:269px">
      <span class="quote-mark">“</span>
      <p>Nunc volutpat fringilla ipsum, a cursus ligula ultrices sed. Aenean in erat ante. Maecenas tincidunt mauris ac massa viverra.</p>
      <span class="stars">★★★★★</span>
      <i class="avatar" role="img" aria-label="Customer portrait"></i>
      <span class="story-name">Dana Holt</span><span class="story-role">Customer</span>
    </article>
    <div class="dots" style="left:192px;top:171px"><i class="on" style="background:var(--teal)"></i><i style="background:#9aa5ab"></i><i style="background:#9aa5ab"></i></div>
  </section>

  <footer class="site-footer">
    <div class="foot-col" style="left:29px">
      <h5>Quick Links</h5>
      <ul><li>Home</li><li>Features</li><li>Pricing</li><li>Register</li><li>Login</li></ul>
    </div>
    <div class="foot-col foot-contact" style="left:114px">
      <h5>Contact Info</h5>
      <ul>
        <li><svg width="4" height="5" viewBox="0 0 4 5"><path d="M2 0a2 2 0 0 0-2 2c0 1.4 2 3 2 3s2-1.6 2-3a2 2 0 0 0-2-2z" fill="#4d8aa3"/></svg><span>45 BC, making it over 2000<br>enim lacinia</span></li>
        <li><svg width="5" height="4" viewBox="0 0 5 4"><rect width="5" height="4" fill="#4d8aa3"/></svg><span>info@molt.io</span></li>
        <li><svg width="5" height="5" viewBox="0 0 5 5"><path d="M1 0l1 1.3-.6.8a3 3 0 0 0 1.5 1.5l.8-.6L5 4l-.7 1C2 5 0 3 0 .7z" fill="#4d8aa3"/></svg><span>1800 555 019</span></li>
      </ul>
    </div>
    <div class="foot-col" style="left:217px">
      <h5>Description Of The Tool</h5>
      <p class="foot-text">Lorem ipsum dsit amr adipiscing elit. Vivamus facilisis placerat mauris. Mauris a lam. Vestibulum imperdiet eros elit</p>
    </div>
    <div class="foot-col" style="left:331px">
      <h5>Get In Touch</h5>
      <div class="social"><i></i><i></i><i></i><i></i></div>
    </div>
    <div class="foot-bar">
      <div class="brand" style="left:8px;top:4px;font-size:11px;color:#3d6676"><i class="brand-dot" style="width:17px;height:17px;background:transparent"></i>MOLT</div>
      <p class="copy">© 2024 <b>MOLT</b>. All right reserved</p>
      <span class="stamp">September 12, 2024. Layout_4</span>
    </div>
  </footer>
</main>

<!-- ============ DASHBOARD ============ -->
<section class="app-panel" style="top:37px;height:266px">
  <header class="app-bar">
    <div class="brand" style="left:5px;top:3px;font-size:12px"><i class="brand-dot" style="width:17px;height:17px"></i>MOLT</div>
    <div class="app-tools">
      <svg width="7" height="6" viewBox="0 0 7 6"><path d="M3.5 0L7 3H6v3H4.3V4H2.7v2H1V3H0z" fill="var(--yellow)"/></svg>
      <span class="lang">Eng ▾</span>
      <span class="icon-btn"></span><span class="icon-btn fill"></span>
      <span class="btn btn-teal logout">Logout</span>
    </div>
  </header>
  <div class="side-card" style="top:51px">
    <div class="side-head">Affected People</div>
    <div class="stat">
      <svg width="14" height="9" viewBox="0 0 14 9"><circle cx="7" cy="2.5" r="2.2" fill="var(--yellow)"/><circle cx="2.5" cy="3.5" r="1.6" fill="var(--yellow)"/><circle cx="11.5" cy="3.5" r="1.6" fill="var(--yellow)"/><path d="M3 9a4 4 0 0 1 8 0zM0 9a2.5 2.5 0 0 1 4-2M14 9a2.5 2.5 0 0 0-4-2" fill="var(--yellow)"/></svg>
      <div><div class="stat-num">1,200,136</div><div class="stat-label">Total Count</div></div>
    </div>
  </div>
  <div class="side-card" style="top:92px;height:82px">
    <div class="side-head">Events Ongoing</div>
    <div class="row-item"><i class="row-icon"></i><div class="row-text"><b style="font-weight:500">Flood:</b> Area Name<small>16 Sep 24, 08:00PM</small></div></div>
    <div class="row-item"><i class="row-icon"></i><div class="row-text"><b style="font-weight:500">Flood:</b> Area Name<small>16 Sep 24, 08:00PM</small></div></div>
    <div class="row-item"><i class="row-icon"></i><div class="row-text"><b style="font-weight:500">Flood:</b> Area Name<small>16 Sep 24, 08:00PM</small></div></div>
  </div>
  <div class="side-card" style="top:181px;height:59px">
    <div class="side-head">Alerts</div>
    <div class="row-item"><i class="row-icon"><svg width="7" height="6" viewBox="0 0 7 6"><path d="M3.5 0L7 6H0z" fill="var(--yellow)"/></svg></i><div class="row-text">Curabitur bibendum,<br>massa vitae elementum</div></div>
    <div class="row-item"><i class="row-icon"><svg width="7" height="6" viewBox="0 0 7 6"><path d="M3.5 0L7 6H0z" fill="var(--yellow)"/></svg></i><div class="row-text">Curabitur bibendum,<br>massa vitae elementum</div></div>
  </div>
  <div class="map" role="img" aria-label="World map of the Atlantic, Americas, Europe and Africa with markers on monitored camps">
    <div class="map-ctrls"><i></i><i></i><i></i><i></i></div>
    <div class="map-ctrls" style="top:135px"><i></i><i></i></div>
    <div class="zoom">+<br>−</div>
  </div>
  <p class="small-copy" style="top:251px">© 2024 <b>MOLT</b>. All right reserved</p>
</section>

<!-- ============ REGISTRATION ============ -->
<section class="app-panel" style="top:343px;height:309px">
  <header class="app-bar">
    <div class="brand" style="left:5px;top:3px;font-size:12px"><i class="brand-dot" style="width:17px;height:17px"></i>MOLT</div>
  </header>
  <form class="reg-card">
    <h2>Register In MOLT</h2>
    <div class="field"><label style="left:11px;top:24px">Enter Your Name</label><span class="input" style="left:11px;top:34px;width:74px">Name</span></div>
    <div class="field"><label style="left:95px;top:24px">Enter Your Surname</label><span class="input" style="left:92px;top:34px;width:75px">Surname</span></div>
    <div class="field"><label style="left:184px;top:24px">Mobile Number</label><span class="input" style="left:184px;top:34px;width:157px">Mobile No.</span></div>

    <div class="field"><label style="left:11px;top:56px">Enter your User Id <span>(Min. 8 Characters)</span></label><span class="input" style="left:11px;top:66px;width:157px">User ID</span></div>
    <div class="field"><label style="left:184px;top:56px">Organization Business Name</label><span class="input" style="left:184px;top:66px;width:157px">Organization Name</span></div>

    <div class="field"><label style="left:11px;top:88px">Enter Password <span>(Min. 8 Characters)</span></label><span class="input" style="left:11px;top:98px;width:157px">********</span></div>
    <div class="field"><label style="left:184px;top:88px">Type of Organization</label><span class="input" style="left:184px;top:98px;width:157px;justify-content:space-between;padding-right:6px">Organization Type<svg width="4" height="2" viewBox="0 0 4 2"><path d="M0 0h4L2 2z" fill="#333"/></svg></span></div>

    <div class="field"><label style="left:11px;top:120px">Enter Valid Email Address</label><span class="input" style="left:11px;top:130px;width:157px">Email address</span></div>
    <div class="field"><label style="left:184px;top:120px">Street</label><span class="input" style="left:184px;top:130px;width:74px">Street Name</span></div>
    <div class="field"><label style="left:267px;top:120px">Number</label><span class="input" style="left:267px;top:130px;width:74px">Number</span></div>

    <div class="field"><label style="left:11px;top:153px">Confirms Email Address</label><span class="input" style="left:11px;top:163px;width:157px">Email address</span></div>
    <div class="field"><label style="left:184px;top:153px">City</label><span class="input" style="left:184px;top:163px;width:74px">Name of City</span></div>
    <div class="field"><label style="left:267px;top:153px">Postal Code</label><span class="input" style="left:267px;top:163px;width:74px">Zip Code</span></div>

    <div class="field"><label style="left:184px;top:185px">Country</label><span class="input" style="left:184px;top:195px;width:74px">Name of City</span></div>
    <div class="field"><label style="left:267px;top:185px">Telephone <span>(Optional)</span></label><span class="input" style="left:267px;top:195px;width:74px">Zip Code</span></div>

    <div class="check" style="top:187px"><i></i>Confirm Terms And Conditions of MOLT</div>
    <div class="check" style="top:198px"><i></i>Confirm Privacy Policy of MOLT</div>
    <div class="btn btn-yellow reg-btn">Register</div>
  </form>
  <p class="small-copy" style="top:295px">© 2024 <b>MOLT</b>. All right reserved</p>
</section>

<!-- ============ MONITOR ============ -->
<section class="app-panel" style="top:696px;height:266px">
  <header class="app-bar">
    <div class="brand" style="left:5px;top:3px;font-size:12px"><i class="brand-dot" style="width:17px;height:17px"></i>MOLT</div>
    <div class="app-tools">
      <svg width="7" height="6" viewBox="0 0 7 6"><path d="M3.5 0L7 3H6v3H4.3V4H2.7v2H1V3H0z" fill="var(--yellow)"/></svg>
      <span class="lang">Eng ▾</span>
      <span class="icon-btn"></span><span class="icon-btn fill"></span>
      <span class="btn btn-teal logout">Logout</span>
    </div>
  </header>
  <aside class="layer-list">
    <div class="side-head">Layer List</div>
    <ul>
      <li>Flooded Areas</li>
      <li>Buildings<svg width="5" height="5" viewBox="0 0 5 5"><rect width="5" height="5" fill="var(--teal)"/><path d="M1.3 1.3l2.4 2.4M3.7 1.3L1.3 3.7" stroke="#fff" stroke-width=".7"/></svg></li>
      <li>Impacts</li>
      <li>Stations</li>
    </ul>
  </aside>
  <div class="map" role="img" aria-label="World map of the Atlantic, Americas, Europe and Africa for layer monitoring">
    <i class="abs" style="left:5px;top:9px;width:12px;height:12px;background:var(--white);border-radius:1.5px"></i>
    <div class="map-toolbar"><i></i><i></i><i></i><i></i><i></i></div>
    <div class="map-ctrls"><i></i><i></i><i></i><i></i></div>
    <div class="map-ctrls" style="top:135px"><i></i><i></i></div>
    <div class="zoom">+<br>−</div>
  </div>
  <p class="small-copy" style="top:255px">© 2024 <b>MOLT</b>. All right reserved</p>
</section>

<p class="thanks thanks-top">THANK YOU FOR</p>
<p class="thanks thanks-big">WATCHING</p>

</body>
</html>
```